Business card design needed for a security services business.

We provide a wide range of security services from guard personnel to electronic systems.

Industry/Entity Type

Security Industry

Contact Information for Business Card

Brent Holloway, Owner Office: 780.555.0148; Cell: 780.555.0193 Email: brent@korvanshieldgroup.example; Address 20417 163 St Edmonton, AB T5X 2K8

Colors
0054AA
0677BA
7BADD7
CADEEF
E8F1F8

Requirements
Nice to have
• On the back of the card I would like to possible list the services I provide: Guards Mobiles Live Video Surveillance Access Intrusion

```html
<!DOCTYPE html>
<html lang="en">
<head>
<meta charset="UTF-8">
<title>Korvan Shield Group – Business Card</title>
<link href="https://fonts.googleapis.com/css2?family=Montserrat:wght@400;500;700&family=Oswald:wght@500&display=swap" rel="stylesheet">
<style>
  :root {
    --blue: #0677BA;
    --blue-deep: #0054AA;
    --ink: #1c1d1f;
    --ink-soft: #2a2b2e;
    --paper: #ffffff;
    --grey-text: #6b6d70;
    --stage: #3a3a3c;
  }
  * { margin: 0; padding: 0; box-sizing: border-box; }
  html, body { width: 1200px; height: 1200px; overflow: hidden; }
  body {
    background: var(--stage);
    font-family: "Montserrat", Arial, sans-serif;
    position: relative;
  }
  .card {
    position: absolute;
    left: 200px;
    width: 800px;
    height: 457px;
    border-radius: 28px;
    overflow: hidden;
  }
  .card--front { top: 100px; background: var(--ink); }
  .card--back  { top: 643px; background: linear-gradient(160deg, var(--ink-soft), var(--ink)); }

  /* front */
  .front__top {
    position: absolute; left: 0; top: 0; width: 100%; height: 262px;
    background: var(--paper);
  }
  .front__stripe {
    position: absolute; left: 0; top: 262px; width: 100%; height: 9px;
    background: var(--blue);
  }
  .brand {
    display: flex; align-items: center; justify-content: center; gap: 14px;
    font-weight: 700; letter-spacing: 2px; color: var(--blue);
    text-transform: uppercase;
  }
  .brand__mark { background: var(--blue); }
  .front .brand { position: absolute; top: 82px; width: 100%; font-size: 40px; }
  .front .brand__mark { width: 26px; height: 26px; }
  .services {
    position: absolute; top: 196px; width: 100%;
    display: flex; justify-content: center; gap: 26px;
    font-family: "Oswald", "Arial Narrow", sans-serif;
    font-weight: 500; font-size: 21px; color: var(--ink);
    text-transform: uppercase; letter-spacing: .3px;
  }
  .services li { list-style: none; }
  .services li::before { content: "• "; color: var(--blue); }

  .contact-person {
    position: absolute; left: 64px; top: 306px;
    border-left: 5px solid var(--blue); padding-left: 16px;
  }
  .contact-person__name {
    font-size: 30px; font-weight: 500; color: var(--blue);
    text-transform: uppercase; line-height: 1.05;
  }
  .contact-person__role {
    font-size: 20px; color: var(--paper); text-transform: uppercase; margin-top: 2px;
  }
  .contact-list { position: absolute; list-style: none; color: var(--paper); }
  .contact-list li {
    display: flex; align-items: center; gap: 12px; font-size: 21px; margin-bottom: 12px;
  }
  .contact-list svg { width: 22px; height: 22px; flex: none; fill: var(--blue); }
  .contact-list--phones { left: 84px; top: 378px; }
  .contact-list--phones li { margin-bottom: 6px; font-size: 24px; }
  .contact-list--details { left: 392px; top: 318px; }
  .contact-list--details li { font-size: 19px; }

  /* back */
  .card--back .brand {
    position: absolute; top: 170px; width: 100%; font-size: 50px;
  }
  .card--back .brand__mark { width: 34px; height: 34px; }
  .back__rule {
    position: absolute; left: 150px; right: 150px; top: 250px; height: 3px;
    background: var(--paper);
  }
  .back__band {
    position: absolute; right: 0; bottom: 0; width: 440px; height: 26px;
    background: linear-gradient(90deg, var(--blue), var(--blue-deep));
  }
</style>
</head>
<body>

<section class="card card--front front" aria-label="Card front">
  <div class="front__top"></div>
  <div class="front__stripe"></div>

  <div class="brand"><span class="brand__mark"></span>Korvan Shield Group</div>

  <ul class="services">
    <li>Guards Mobiles</li>
    <li>Live Video Surveillance</li>
    <li>Access Intrusion</li>
  </ul>

  <div class="contact-person">
    <p class="contact-person__name">Brent Holloway</p>
    <p class="contact-person__role">Owner</p>
  </div>

  <ul class="contact-list contact-list--phones">
    <li>
      <svg viewBox="0 0 24 24" aria-hidden="true"><path d="M6.6 10.8a15.1 15.1 0 0 0 6.6 6.6l2.2-2.2a1 1 0 0 1 1-.25 11.4 11.4 0 0 0 3.6.57 1 1 0 0 1 1 1V20a1 1 0 0 1-1 1A17 17 0 0 1 3 4a1 1 0 0 1 1-1h3.5a1 1 0 0 1 1 1c0 1.25.2 2.45.57 3.6a1 1 0 0 1-.25 1z"/></svg>
      780.555.0148
    </li>
    <li>
      <svg viewBox="0 0 24 24" aria-hidden="true"><path d="M7 1h10a2 2 0 0 1 2 2v18a2 2 0 0 1-2 2H7a2 2 0 0 1-2-2V3a2 2 0 0 1 2-2zm0 3v14h10V4zm5 15.5a1 1 0 1 0 0 2 1 1 0 0 0 0-2z"/></svg>
      780.555.0193
    </li>
  </ul>

  <ul class="contact-list contact-list--details">
    <li>
      <svg viewBox="0 0 24 24" aria-hidden="true"><path d="M2 5h20v14H2zm2 2v.4l8 5.2 8-5.2V7zm0 2.8V17h16V9.8l-8 5.2z"/></svg>
      brent@korvanshieldgroup.example
    </li>
    <li>
      <svg viewBox="0 0 24 24" aria-hidden="true"><path d="M12 2a7 7 0 0 0-7 7c0 5.2 7 13 7 13s7-7.8 7-13a7 7 0 0 0-7-7zm0 9.5A2.5 2.5 0 1 1 12 6.5a2.5 2.5 0 0 1 0 5z"/></svg>
      20417 163 St Edmonton, AB T5X 2K8
    </li>
  </ul>
</section>

<section class="card card--back" aria-label="Card back">
  <div class="brand"><span class="brand__mark"></span>Korvan Shield Group</div>
  <div class="back__rule"></div>
  <div class="back__band"></div>
</section>

</body>
</html>
```